Exciting opportunity to create logo and a label for our natural health brand.

About us

We are a customer centric health supplement brand who believes in natural medicine and high quality ingredients. We take a holistic approach to healthcare, with an eastern philosophy. We believe in being partners with our customers in their health care journey and are invested in their well being.

Our brand philosophy and values are attached (see Varo philosophy.png). Our personality traits are:

- Natural
- Fresh
- Modern
- Balanced (in a holistic sense)

Task breakdown

1. Design a fresh feeling logo for us
- We want it to represent our values and high quality ingredients. We would like the quality of the product to be reflected in the branding and have a high end feel.
- Logo text must include Varo Health Sciences
- We want the Varo to be the focus of the logo (see uploaded image Varo logo example.png)
The logo does not have to follow this layout, but we just want the Varo to stand out. Feel free to use your creative license on this!

2. Create an attractive label to go on the supplement bottle
- The designs need to be eye catching, give a sense of high end ingredients and natural products and tie in with the logo to give a joined up feel.
- We are selling our products online and need them to really stand out from the competition.
- See examples of labels and packaging we like (1 -7 label design).

The initial label we would like you to design would be for our product Calm Haven. It is a product that assists in the management of Anxiety and stress. The label will appear on the bottle that holds the capsules for this supplement, see uploaded files (Example plain bottles.png). The bottles may be white as the picture shows or dark blue recyclable plastic or dark brown glass . We don't have the exact dimensions of the bottle yet, but I will follow up with these.

The label needs to include the following things:
1. The logo
2. The name of the product
3. The product is to help with the relief of Anxiety and Stress
4. Number of capsules the bottle contains
5. The back of the label should have
i) The ingredients
ii) Dosage
iii) Directions of use

Please use placeholder text where needed.

We look forward to seeing your design. Thank you.

```html
<!DOCTYPE html>
<html lang="en">
<head>
<meta charset="utf-8">
<title>Varo Health Sciences – Calm Haven Label</title>
<link href="https://fonts.googleapis.com/css2?family=Montserrat:wght@400;500;700&family=Source+Serif+4:wght@300&display=swap" rel="stylesheet">
<style>
  :root {
    --label-bg: #dce7d2;
    --band: #b5cea5;
    --leaf-tone: #c4d8b4;
    --leaf-light: #e8efe1;
    --brand-green: #17691f;
    --ink: #111111;
    --white: #ffffff;
  }
  html, body {
    margin: 0;
    padding: 0;
    width: 1200px;
    height: 375px;
    overflow: hidden;
    background: var(--label-bg);
  }
  .label {
    position: relative;
    width: 1200px;
    height: 375px;
    background: var(--label-bg);
    overflow: hidden;
    font-family: "Montserrat", Arial, sans-serif;
    color: var(--ink);
  }
  .foliage {
    position: absolute;
    border-radius: 50%;
  }
  .foliage--left {
    left: 240px; top: 85px; width: 265px; height: 300px;
    background: radial-gradient(ellipse at 45% 55%, var(--leaf-tone) 0%, rgba(196,216,180,0.35) 45%, rgba(220,231,210,0) 72%);
  }
  .foliage--top {
    left: 550px; top: -40px; width: 260px; height: 220px;
    background: radial-gradient(ellipse at 50% 45%, var(--leaf-light) 0%, rgba(232,239,225,0.5) 45%, rgba(220,231,210,0) 72%);
  }
  .foliage--right {
    left: 915px; top: 185px; width: 300px; height: 190px;
    background: radial-gradient(ellipse at 60% 55%, var(--leaf-tone) 0%, rgba(196,216,180,0.35) 45%, rgba(220,231,210,0) 72%);
  }
  .base-band {
    position: absolute;
    left: 0; top: 0;
  }

  /* Nutrition panel */
  .nutrition {
    position: absolute;
    left: 23px; top: 0;
    width: 208px;
    height: 240px;
  }
  .nutrition > * { position: absolute; margin: 0; white-space: nowrap; }
  .nutrition__title {
    left: 3px; top: 41px;
    font-size: 25px; font-weight: 700; letter-spacing: 0.3px;
  }
  .nutrition__meta { left: 4px; font-size: 7.5px; line-height: 10px; }
  .nutrition__meta span { display: inline-block; width: 68px; }
  .rule { left: 0; width: 208px; background: var(--ink); height: 0.6px; }
  .rule--heavy { height: 3px; }
  .rule--mid { height: 1.6px; }
  .row { left: 4px; width: 200px; font-size: 6.5px; line-height: 9px; display: flex; justify-content: space-between; }
  .row--indent { left: 10px; }
  .row--head { font-size: 7.5px; font-weight: 700; }
  .row--calories { font-size: 7.5px; }
  .row--dv { justify-content: flex-end; padding-right: 24px; width: 176px; }
  .row--dv span, .row .dv { padding-right: 2px; }
  .nutrition__strong { left: 4px; font-size: 6.5px; font-weight: 700; line-height: 9px; }

  /* Brand lockup */
  .brand {
    position: absolute;
    left: 466px; top: 92px;
    width: 140px;
    text-align: center;
    color: var(--brand-green);
    font-weight: 500;
  }
  .brand__name {
    display: block;
    font-size: 54px; line-height: 60px; letter-spacing: -1px;
  }
  .brand__sub {
    display: block;
    font-size: 10px; line-height: 12px; letter-spacing: 0.2px;
  }
  .brand__dot {
    position: absolute;
    left: 584px; top: 126px;
    width: 14px; height: 14px;
    border-radius: 50%;
    background: var(--brand-green);
  }

  /* Product name */
  .product__rule {
    position: absolute; height: 1.5px; background: var(--white);
  }
  .product__rule--top { left: 463px; top: 195px; width: 153px; }
  .product__rule--bottom { left: 463px; top: 239px; width: 65px; }
  .product__name {
    position: absolute; left: 440px; top: 192px; margin: 0;
    font-family: "Source Serif 4", Georgia, serif;
    font-weight: 300; font-size: 36px; line-height: 46px;
    color: var(--white); white-space: nowrap;
  }
  .product__benefit {
    position: absolute; left: 535px; top: 236px; margin: 0;
    font-size: 6px; line-height: 8px; color: var(--brand-green); white-space: nowrap;
  }
  .product__count {
    position: absolute; left: 510px; top: 323px; margin: 0;
    font-size: 8px; line-height: 10px; letter-spacing: 0.3px; color: var(--brand-green);
  }
  .product__weight {
    position: absolute; left: 493px; top: 354px; margin: 0;
    font-size: 7.5px; line-height: 10px; color: var(--white);
  }

  /* Directions */
  .directions {
    position: absolute; left: 936px; top: 78px; width: 240px;
    font-size: 8px; line-height: 10px; color: var(--ink);
  }
  .directions__title { margin: 0 0 23px; font-size: 8.5px; font-weight: 400; }
  .directions p { margin: 0 0 10px; }
</style>
</head>
<body>
<main class="label">
  <div class="foliage foliage--left" role="img" aria-label="Line-drawn botanical leaves, soft green"></div>
  <div class="foliage foliage--top" role="img" aria-label="Faint white line-drawn leaves"></div>
  <div class="foliage foliage--right" role="img" aria-label="Line-drawn botanical leaves, soft green"></div>

  <svg class="base-band" width="1200" height="375" viewBox="0 0 1200 375" aria-hidden="true">
    <polygon points="478,342 1200,342 1200,375 445,375" fill="var(--band)"/>
  </svg>

  <section class="nutrition" aria-label="Nutrition facts">
    <h2 class="nutrition__title">Nutrition Facts</h2>
    <p class="nutrition__meta" style="top:71px"><span>Serving Size</span>8 fl oz (240 mL)</p>
    <p class="nutrition__meta" style="top:82px"><span style="width:101px">Servings per Container</span>2</p>
    <div class="rule rule--heavy" style="top:95px"></div>
    <p class="row row--head" style="top:102px">Amount Per Serving</p>
    <div class="rule" style="top:112.5px"></div>
    <p class="row row--calories" style="top:115px">Calories&nbsp;&nbsp;&nbsp;37</p>
    <div class="rule rule--mid" style="top:127px"></div>
    <p class="row row--dv" style="top:131px"><span>% Daily Value</span></p>
    <div class="rule" style="top:141px"></div>
    <p class="row" style="top:142px"><span>Total Fat&nbsp;&nbsp;0g</span><span class="dv">0%</span></p>
    <div class="rule" style="top:151px"></div>
    <p class="row" style="top:153px"><span>Sodium&nbsp;&nbsp;10mg</span><span class="dv">0%</span></p>
    <div class="rule" style="top:163px"></div>
    <p class="row" style="top:164.5px"><span>Total Carbohydrate&nbsp;&nbsp;&nbsp;8g</span><span class="dv">3%</span></p>
    <div class="rule" style="top:174px"></div>
    <p class="row row--indent" style="top:174.5px"><span>Sugars&nbsp;&nbsp;6g</span></p>
    <div class="rule" style="top:184px"></div>
    <p class="row" style="top:186px"><span>Protein&nbsp;&nbsp;less than 1g</span></p>
    <div class="rule rule--heavy" style="top:197px"></div>
    <p class="nutrition__strong" style="top:204px">Probiotic Content</p>
    <p class="row" style="top:212px"><span>Lactobacillius Bacterium: 1 Billion Organisms</span></p>
    <p class="nutrition__strong" style="top:224px">Ingredients</p>
  </section>

  <div class="brand">
    <span class="brand__name">Varo</span>
    <span class="brand__sub">HEALTH SCIENCES</span>
  </div>
  <span class="brand__dot" aria-hidden="true"></span>

  <div class="product__rule product__rule--top"></div>
  <h1 class="product__name">Calm Haven</h1>
  <div class="product__rule product__rule--bottom"></div>
  <p class="product__benefit">ANXIETY + STRESS RELIEF</p>
  <p class="product__count">60 CAPSULES</p>
  <p class="product__weight">NET WT. 10 oz (lorem ip)</p>

  <section class="directions">
    <h2 class="directions__title">DIRECTIONS |</h2>
    <p>Lorem ipsum dolor sit amet, consectetur adipiscing elit. Fusce in lacinia velit, sit amet congue ipsum. Nunc cursus facilisis dui, sed suscipit mi malesuada eget. Ut lorem urna, hendrerit et dolor at, euismod accumsan dolor.</p>
    <p>Praesent dignissim neque vel neque sodales lacinia. Maecenas aliquet ex et vulputate sagittis. In sodales mauris eu interdum sollicitudin. Proin pulvinar convallis fringilla. Aliquam auctor commodo placerat. Mauris nec lacus vitae mi euismod biben dum.</p>
  </section>
</main>
</body>
</html>
```